Redesign Teeth Whitening Flyer

I need to redesign this flyer attached. I have upgraded the kit. Logo attached and current design uploaded. I have new content etc that I will provide in the brief. Here is a competitor of mine that does well https://www.shopvandle.com/Frost-Teeth-Whitening-At-Home-Sensitivity/dp/K42QX81M7R

The size will be full bleed: 7.875" X 4.375"

FULL COLOR
Front & Back

FRONT SIDE:
~~LUMO LOGO~~
~~PLEASE INTEGRATE PHOTOS OF THE PRODUCT I HAVE ATTACHED. I GOT THESE PHOTOS FROM THE MANUFACTURERS WEBSITES. PLEASE KEEP IN MIND THIS WILL BE PRINTED~~

CONTENT:
ADVANCED TEETH WHITENING SYSTEM
15 TREATMENTS INCLUDED

BACK SIDE CONTENT:
Thank you for your purchase of Lumo Professional Teeth Whitening products. All of our whitening solutions are manufactured in a FDA registered facility in the USA.

We provide effective and affordable teeth whitening solutions using the highest quality ingredients available.

Directions:

Step 1
Rinse the Glowfit Tray with warm water.

Step 2
Apply whitening solution to your teeth. Rotate the pen at the base to dispense the gel onto the brush. Make a big wide smile and apply the gel generously to the teeth using the brush. Be sure to apply the whitening gel to the front of the teeth only.

Step 3
Connect the Glowfit Tray to any smart device or power bank of your choice and turn it on so that the LED light is constant.

Step 4
Put the Glowfit Tray into your mouth and bite down firmly. Keep the tray in your mouth for 20-30 minutes.

Step 5
Remove the tray from your mouth and rinse your mouth and tray with lukewarm water and allow the tray to dry before storing it.

There are up to 15 treatments included with one pen.

We recommend when using the system for the first time to use it daily until desired results are achieved. Then reduce to 1-2 times per week to maintain.

To get more whitening solution pens please go to www.LumoTeethWhitening.example

DISCLAIMERS:
Keep out of reach of children. Avoid contact with eyes and skin. Consult your dentist before using. Do not use if pregnant, lactating, have gum disease or other dental conditions. Discontinue use if pain on teeth or gums occurs. Use only as instructed. Use at your own risk. Purchasing any of our products frees all distributors, manufacturers and affiliates from any liability associated with the use of this system. Do not use if you are allergic to peroxide products. The whitening solution is a 12% Hydrogen Peroxide whitening solution. 12% HP is equivalent to 36% Carbamide Peroxide. A temporary side effect of tooth sensitivity or mild tissue irritation is possible but usually transient and may last for a day or two. Avoid beverages that contain citrus and hot and cold drinks for the next 24 hours after treatment. Sticking to room temperature drinks is ideal. If you have any adverse reactions terminate the use of this product and consult a healthcare professional.

Target Market(s)

consumers that are interested in teeth whitening home kits. DIY teeth whitening at home

Font styles to use
Other font styles liked:
• open

Requirements
Must have
• FULL COLOR
Front & Back

FRONT SIDE:
~~LUMO LOGO~~

CONTENT:
15 TREATMENTS INCLUDED

BACK SIDE CONTENT:

Directions:

Step 1

Step 2

Step 3

Step 4

Step 5

DISCLAIMERS:
Nice to have
• FULL COLOR
Front & Back

FRONT SIDE:
~~LUMO LOGO~~

CONTENT:
15 TREATMENTS INCLUDED

BACK SIDE CONTENT:

Directions:

Step 1

Step 2

Step 3

Step 4

Step 5

DISCLAIMERS:

```html
<!DOCTYPE html>
<html lang="en">
<head>
<meta charset="utf-8">
<title>Lumo Whitening Insert – Front and Back</title>
<link rel="stylesheet" href="https://fonts.googleapis.com/css2?family=Lexend:wght@700;800&family=Open+Sans:wght@400;600;700&display=swap">
<style>
  :root{
    --teal:#1aaec9;
    --teal-dark:#1597b0;
    --white:#ffffff;
    --ink:#2b2b2b;
    --backdrop:#e3f1fa;
    --photo-a:#dcdcdc;
    --photo-b:#c9c6c4;
    --product-a:#f4f7f9;
    --product-b:#d7e6ee;
  }
  *{box-sizing:border-box;margin:0;padding:0}
  html,body{width:1200px;height:1200px;overflow:hidden}
  body{background:var(--backdrop);font-family:"Open Sans",Arial,sans-serif;position:relative}

  .card{position:absolute;top:173px;background:var(--teal);overflow:hidden;box-shadow:0 4px 14px rgba(40,80,110,.18)}
  .card--front{left:86px;width:475px;height:854px}
  .card--back{left:640px;width:477px;height:858px;background:var(--white)}

  .card__wave{position:absolute;left:0;top:0;width:100%;height:170px}

  .brand-name{position:absolute;left:0;right:0;text-align:center;font-family:"Open Sans",Arial,sans-serif;
    font-weight:600;font-size:22px;line-height:26px;letter-spacing:1px;text-transform:uppercase}
  .card--front .brand-name{top:48px;color:var(--ink)}
  .card--back .brand-name{top:48px;color:var(--white)}

  .hero-photo{position:absolute;left:57px;top:190px;width:363px;height:388px;border:2px solid var(--white);
    border-radius:160px 160px 40px 40px;padding:12px}
  .hero-photo__fill{width:100%;height:100%;border-radius:148px 148px 30px 30px;
    background:linear-gradient(160deg,var(--photo-a),var(--photo-b))}

  .product-row{position:absolute;left:42px;top:596px;width:393px;height:100px;display:flex;justify-content:space-between}
  .product-thumb{width:90px;height:100px;border-radius:34px 34px 14px 14px;
    background:linear-gradient(160deg,var(--product-a),var(--product-b))}

  .headline{position:absolute;left:0;right:0;top:708px;text-align:center;color:var(--white);
    font-family:"Lexend",Arial,sans-serif;font-weight:800;font-size:39px;line-height:37px;letter-spacing:.2px}
  .treatments{position:absolute;left:64px;right:64px;top:797px;height:34px;border:2px solid var(--white);border-top:none;
    text-align:center}
  .treatments span{position:relative;top:14px;background:var(--teal);padding:0 6px;color:var(--white);
    font-family:"Lexend",Arial,sans-serif;font-weight:700;font-size:21px;line-height:24px}

  .back-body{position:absolute;left:0;right:0;top:170px;color:var(--teal);font-size:9.9px;line-height:13.6px}
  .back-body .center{text-align:center;font-weight:700}
  .back-body .intro{margin-top:2px}
  .back-body .mission{margin-top:8px;padding:0 40px}
  .directions{margin:21px 0 0 29px;width:420px}
  .directions h2{font-size:9.9px;font-weight:700;margin-bottom:14px}
  .step{margin-bottom:14px}
  .step h3{font-size:9.9px;font-weight:700}
  .back-body .note{margin-top:0}
  .back-body .recommend{margin-top:14px;padding:0 20px}
  .back-body .more{margin-top:13px}
  .url-pill{display:block;width:200px;height:20px;margin:10px auto 0;border-radius:10px;background:var(--teal);
    color:var(--white);font-weight:700;text-align:center;line-height:20px;font-size:10px}

  .disclaimer{position:absolute;left:0;right:0;bottom:0;height:180px;background:var(--teal);color:var(--white);
    text-align:center;font-size:8.9px;line-height:13.6px;padding:6px 24px 0}
  .disclaimer h2{font-size:8.9px;font-weight:400}
</style>
</head>
<body>

  <section class="card card--front" aria-label="Front side">
    <svg class="card__wave" viewBox="0 0 475 170" preserveAspectRatio="none" aria-hidden="true">
      <path d="M0 0H475V110Q237 205 0 110Z" fill="#ffffff"/>
    </svg>
    <p class="brand-name">Coastline Smile<br>Whitening Studio</p>

    <div class="hero-photo">
      <div class="hero-photo__fill" role="img" aria-label="Photo of a smiling couple embracing, showing white teeth"></div>
    </div>

    <div class="product-row">
      <div class="product-thumb" role="img" aria-label="Product photo: LED tray connected to a phone with whitening pen"></div>
      <div class="product-thumb" role="img" aria-label="Product photo: kit box with whitening pen"></div>
      <div class="product-thumb" role="img" aria-label="Product photo: LED tray with charging cable"></div>
      <div class="product-thumb" role="img" aria-label="Product photo: close-up of the clear LED tray"></div>
    </div>

    <h1 class="headline">ADVANCED TEETH<br>WHITENING SYSTEM</h1>
    <div class="treatments"><span>15 TREATMENTS INCLUDED</span></div>
  </section>

  <section class="card card--back" aria-label="Back side">
    <svg class="card__wave" viewBox="0 0 477 170" preserveAspectRatio="none" aria-hidden="true">
      <path d="M0 0H477V110Q238 205 0 115Z" fill="#1aaec9"/>
    </svg>
    <p class="brand-name">Coastline Smile<br>Whitening Studio</p>

    <div class="back-body">
      <p class="center intro">Thank you for your purchase of Lumo Professional Teeth Whitening products.<br>All of our whitening solutions are manufactured in a FDA registered facility in the USA.</p>
      <p class="center mission">We provide effective and affordable teeth whitening solutions using the highest quality ingredients available.</p>

      <div class="directions">
        <h2>Directions:</h2>
        <div class="step"><h3>Step 1</h3><p>Rinse the Glowfit Tray with warm water.</p></div>
        <div class="step"><h3>Step 2</h3><p>Apply whitening solution to your teeth. Rotate the pen at the base to dispense the gel onto the brush. Make a big wide smile and apply the gel generously to the teeth using the brush. Be sure to apply the whitening gel to the front of the teeth only.</p></div>
        <div class="step"><h3>Step 3</h3><p>Connect the Glowfit Tray to any smart device or power bank of your choice and turn it on so that the LED light is constant.</p></div>
        <div class="step"><h3>Step 4</h3><p>Put the Glowfit Tray into your mouth and bite down firmly. Keep the tray in your mouth for 20-30 minutes.</p></div>
        <div class="step"><h3>Step 5</h3><p>Remove the tray from your mouth and rinse your mouth and tray with lukewarm water and allow the tray to dry before storing it.</p></div>
      </div>

      <p class="center note">There are up to 15 treatments included with one pen.</p>
      <p class="center recommend">We recommend when using the system for the first time to use it daily until desired results are achieved. Then reduce to 1-2 times per week to maintain.</p>
      <p class="center more">To get more whitening solution pens please go to</p>
      <span class="url-pill">www.LumoTeethWhitening.example</span>
    </div>

    <div class="disclaimer">
      <h2>DISCLAIMERS:</h2>
      <p>Keep out of reach of children. Avoid contact with eyes and skin. Consult your dentist before using. Do not use if pregnant, lactating, have gum disease or other dental conditions. Discontinue use if pain on teeth or gums occurs. Use only as instructed. Use at your own risk. Purchasing any of our products frees all distributors, manufacturers and affiliates from any liability associated with the use of this system. Do not use if you are allergic to peroxide products. The whitening solution is a 12% Hydrogen Peroxide whitening solution. 12% HP is equivalent to 36% Carbamide Peroxide. A temporary side effect of tooth sensitivity or mild tissue irritation is possible but usually transient and may last for a day or two. Avoid beverages that contain citrus and hot and cold drinks for the next 24 hours after treatment. Sticking to room temperature drinks is ideal. If you have any adverse reactions terminate the use of this product and consult a healthcare professional.</p>
    </div>
  </section>

</body>
</html>
```